Animal Hospital Business Cards

Make a business card look like the attached example

*Use the same blue/black coloring
*Brisket Hollow Animal Hospital (instead of pet home rounds)
*Emergency Services (instead of tamsin creek clinic)
*House Calls (instead of open 7 days by appointment)
*Change address to 278 Brisket Hollow Rd Quillmoor, ND 58263
*Open 7 days a week (instead of emergency service)
*Add the website www.briskethollowanimalhospital.example

On the back...
*instead of the text outlined in red, just white
*instead of the light blue, try your best to make it just like the blue and black on the front side of the card
*Delete "designed and printed by 9 whiskers inc, www.pressfeline.example

Requirements
Must have
• look just like the attached example with requested edits/changes

```html
<!DOCTYPE html>
<html lang="en">
<head>
<meta charset="utf-8">
<title>Brisket Hollow Animal Hospital – Business Card</title>
<link rel="stylesheet" href="https://fonts.googleapis.com/css2?family=Roboto+Condensed:wght@400;700&family=Open+Sans:wght@700&display=swap">
<style>
  :root {
    --blue-deep: #0a5aa8;
    --blue-mid: #1f78c4;
    --blue-light: #6fb0e0;
    --black: #161616;
    --grey: #b9bcc0;
    --white: #ffffff;
    --ink: #1c1c1c;
    --line-blue: #3f7fd0;
    --page: #e9ebee;
  }
  * { box-sizing: border-box; margin: 0; padding: 0; }
  html, body { width: 1154px; height: 1200px; overflow: hidden; }
  body {
    background: var(--page);
    font-family: "Roboto Condensed", "Arial Narrow", sans-serif;
    color: var(--ink);
    position: relative;
  }
  .card {
    position: absolute;
    left: 137px;
    width: 880px;
    height: 480px;
    border-radius: 24px;
    background: var(--white);
    overflow: hidden;
    box-shadow: 0 6px 18px rgba(0,0,0,.18);
  }
  .card--front { top: 70px; }
  .card--back { top: 650px; }

  .band {
    position: absolute; left: 0; right: 0;
    background: linear-gradient(100deg, var(--blue-deep) 0%, var(--blue-mid) 30%, var(--blue-light) 52%, var(--blue-mid) 72%, var(--blue-deep) 100%);
    color: var(--white);
    text-align: center;
  }
  .band--top { top: 0; height: 95px; }
  .band--bottom { bottom: 0; height: 70px; }
  .stripe {
    position: absolute; left: 0; right: 0;
    background: var(--black);
  }
  .stripe--top { top: 95px; border-bottom: 7px solid var(--grey); height: 27px; }
  .stripe--bottom { bottom: 70px; border-top: 7px solid var(--grey); height: 27px; }

  .card-title {
    font-weight: 700;
    font-size: 52px;
    line-height: 95px;
    letter-spacing: .5px;
    text-transform: uppercase;
  }

  /* front */
  .vet-name {
    position: absolute; top: 132px; left: 0; right: 0;
    text-align: center;
    font-family: "Open Sans", sans-serif;
    font-weight: 700; font-size: 36px; letter-spacing: .3px;
  }
  .vet-name small { font-size: 21px; }
  .logo-mark {
    position: absolute; top: 190px; left: 395px;
    width: 90px; height: 90px;
  }
  .service {
    position: absolute;
    font-weight: 700; font-size: 24px; line-height: 28px;
    text-transform: uppercase; text-align: center;
  }
  .service--emergency { left: 60px; top: 200px; }
  .service--house { right: 75px; top: 185px; }
  .species {
    position: absolute; top: 290px; left: 0; right: 0;
    text-align: center;
    font-family: "Open Sans", sans-serif;
    font-weight: 700; font-size: 22px; text-transform: uppercase;
  }
  .species .dot { color: var(--blue-mid); margin: 0 6px; }
  .phone {
    position: absolute; top: 322px; left: 0; right: 0;
    text-align: center;
    font-family: "Open Sans", sans-serif;
    font-weight: 700; font-size: 34px; color: var(--blue-mid);
    letter-spacing: 1px;
  }
  .address {
    position: absolute; left: 40px; top: 332px;
    font-style: normal;
    font-weight: 700; font-size: 19px; line-height: 22px;
    text-transform: uppercase;
  }
  .experience {
    position: absolute; right: 40px; top: 325px;
    font-weight: 700; font-size: 19px; line-height: 22px;
    text-transform: uppercase; text-align: center;
  }
  .hours {
    font-weight: 700; font-size: 32px; line-height: 40px;
    text-transform: uppercase; padding-top: 4px;
  }
  .website {
    font-family: "Open Sans", sans-serif;
    font-weight: 700; font-size: 16px; line-height: 20px;
  }

  /* back */
  .appt-line {
    position: absolute; left: 40px; right: 40px; top: 150px;
    display: flex; align-items: flex-end; gap: 8px;
    font-size: 36px;
  }
  .blank {
    flex: 1; border-bottom: 2px solid var(--line-blue); margin-bottom: 9px;
  }
  .blank--date { flex: 0 0 215px; }
  .blank--time { flex: 0 0 225px; }
  .days {
    position: absolute; left: 31px; top: 240px;
    display: flex; gap: 8px; list-style: none;
  }
  .day {
    width: 110px; height: 44px; border-radius: 22px;
    background: var(--blue-mid);
    color: var(--white);
    font-size: 19px; font-weight: 400;
    text-transform: uppercase;
    display: flex; align-items: center; justify-content: center;
  }
  .date-line { top: 305px; gap: 10px; }
  .date-line .spacer { width: 14px; }
  .meridiem {
    font-size: 15px; line-height: 18px; margin-bottom: 6px; margin-left: 10px;
  }
  .back-name {
    font-family: "Open Sans", sans-serif;
    font-weight: 700; font-size: 26px; line-height: 38px; padding-top: 4px;
    text-transform: uppercase;
  }
  .back-name small { font-size: 16px; }
  .back-phone {
    font-family: "Open Sans", sans-serif;
    font-weight: 700; font-size: 17px; line-height: 20px; letter-spacing: 1px;
  }
</style>
</head>
<body>

<section class="card card--front" aria-label="Business card front">
  <header class="band band--top">
    <h1 class="card-title">Brisket Hollow Animal Hospital</h1>
  </header>
  <div class="stripe stripe--top"></div>

  <p class="vet-name">CORWIN D. ASHDALE, <small>DVM</small></p>
  <svg class="logo-mark" viewBox="0 0 90 90" role="img" aria-label="Hospital logo mark">
    <circle cx="45" cy="45" r="42" fill="#1f78c4"/>
  </svg>
  <p class="service service--emergency">Emergency<br>Services</p>
  <p class="service service--house">House<br>Calls</p>
  <p class="species">Cats<span class="dot">•</span>Dogs<span class="dot">•</span>Birds<span class="dot">•</span>Exotics</p>
  <p class="phone">(555) 201-4837</p>
  <address class="address">278 Brisket Hollow Rd<br>Quillmoor, ND 58263</address>
  <p class="experience">30 Years<br>of Experience</p>

  <div class="stripe stripe--bottom"></div>
  <footer class="band band--bottom">
    <p class="hours">Open 7 Days a Week</p>
    <p class="website">www.briskethollowanimalhospital.example</p>
  </footer>
</section>

<section class="card card--back" aria-label="Appointment card back">
  <header class="band band--top">
    <h2 class="card-title">Veterinary Appointment</h2>
  </header>
  <div class="stripe stripe--top"></div>

  <p class="appt-line"><span>Your appointment for</span><span class="blank"></span><span>is on</span></p>
  <ul class="days">
    <li class="day">Monday</li>
    <li class="day">Tuesday</li>
    <li class="day">Wednesday</li>
    <li class="day">Thursday</li>
    <li class="day">Friday</li>
    <li class="day">Saturday</li>
    <li class="day">Sunday</li>
  </ul>
  <p class="appt-line date-line">
    <span>Date</span><span class="blank blank--date"></span>
    <span class="spacer"></span>
    <span>Time</span><span class="blank blank--time"></span>
    <span class="meridiem">AM<br>PM</span>
  </p>

  <div class="stripe stripe--bottom"></div>
  <footer class="band band--bottom">
    <p class="back-name">Corwin D. Ashdale, <small>DVM</small></p>
    <p class="back-phone">(555) 201-4837</p>
  </footer>
</section>

</body>
</html>
```